Very High End Grooming Salon needs new business card design

I need a very nice card design I am a certified Master groomer we have a very high end clients. Our color is pink but does not have to be pink. I have a logo also a mission statement .
Fern N Fluff Pet Boutique and Spa
48710 Orchard Rd
Harbor Glen fl 30912
555 904 3826
www.fernfluffboutique-example.com
online booking available
this is our mission statement not sure it need to go on card but here it is.
Our Mission is to show respect to all animals pampering them with the same high end tailored service one would expect to receive at a day spa
as the only certified master groomer in the area we strive to put your pets best paw forward.

Industry/Entity Type

Business

```html
<!DOCTYPE html>
<html lang="en">
<head>
<meta charset="utf-8">
<title>Fern N Fluff Pet Boutique and Spa — Business Card</title>
<link rel="stylesheet" href="https://fonts.googleapis.com/css2?family=Lobster+Two:ital,wght@0,700;1,700&family=Courier+Prime&display=swap">
<style>
  :root {
    --page-bg: #efedee;
    --card-white: #ffffff;
    --band-rose: #c9637f;
    --pocket-pink: #d982b8;
    --pocket-edge: #8c4b6c;
    --text-magenta: #d0186c;
    --text-violet: #7a3590;
    --stripe-blush: #f3dde8;
    --icon-grey: #c9c9cc;
    --mark-blush: #f6c6dc;
  }
  * { margin: 0; padding: 0; box-sizing: border-box; }
  html, body {
    width: 1200px; height: 817px; overflow: hidden;
    background: var(--page-bg);
  }
  .card {
    position: absolute; left: 160px; top: 158px;
    width: 880px; height: 500px;
    background: var(--card-white);
    box-shadow: 0 6px 24px rgba(0,0,0,0.12);
    overflow: hidden;
  }
  .card-shapes { position: absolute; inset: 0; }
  .decor-stripes { position: absolute; left: 360px; top: 80px; }
  .scissors-icon { position: absolute; left: 300px; top: 96px; }
  .brand {
    position: absolute; left: 50px; top: 64px; width: 260px;
    text-align: center;
    font-family: "Lobster Two", cursive;
    font-weight: 700;
    color: var(--text-magenta);
  }
  .brand-mark {
    width: 52px; height: 52px; border-radius: 50%;
    background: var(--mark-blush);
    margin: 0 auto 8px;
  }
  .brand-name { font-size: 30px; line-height: 1.05; }
  .brand-tagline { font-size: 18px; line-height: 1.2; margin-top: 4px; }
  .contact {
    position: absolute; left: 390px; top: 160px;
    list-style: none;
    font-family: "Lobster Two", cursive;
    font-style: italic; font-weight: 700;
    font-size: 30px;
    color: var(--text-magenta);
  }
  .contact li { margin-bottom: 24px; white-space: nowrap; }
  .contact li:nth-child(2) { padding-left: 12px; }
  .contact li:nth-child(3) { padding-left: 22px; }
  .web {
    position: absolute; left: 46px; top: 410px; width: 290px;
    font-family: "Courier Prime", monospace;
    color: var(--text-violet);
    text-align: center;
  }
  .web-address { font-size: 13.5px; white-space: nowrap; }
  .web-note { font-size: 12px; }
</style>
</head>
<body>
  <div class="card">
    <svg class="card-shapes" width="880" height="500" viewBox="0 0 880 500" aria-hidden="true">
      <defs>
        <linearGradient id="stripeFade" x1="0" y1="0" x2="0" y2="1">
          <stop offset="0" stop-color="#ffffff"/>
          <stop offset="0.5" stop-color="#f3dde8"/>
          <stop offset="1" stop-color="#ffffff"/>
        </linearGradient>
      </defs>
      <path class="top-band" d="M0 0 H880 V30 Q600 44 300 52 Q150 56 0 42 Z" fill="var(--band-rose)"/>
      <rect class="pocket" x="40" y="170" width="300" height="300" fill="var(--pocket-pink)" stroke="var(--pocket-edge)" stroke-width="1.5"/>
      <path class="pocket-flap" d="M39 58 H341 V170 Q190 360 39 170 Z" fill="var(--card-white)"/>
    </svg>

    <svg class="decor-stripes" role="img" aria-label="Faint vertical blush stripes decoration" width="460" height="380">
      <rect width="460" height="380" fill="url(#stripeFade)" opacity="0.7"/>
    </svg>

    <svg class="scissors-icon" role="img" aria-label="Small grooming scissors illustration" width="34" height="52">
      <rect width="34" height="52" rx="4" fill="var(--icon-grey)"/>
    </svg>

    <div class="brand">
      <div class="brand-mark"></div>
      <div class="brand-name">Fern N Fluff</div>
      <div class="brand-tagline">Pet Boutique and Spa</div>
    </div>

    <ul class="contact">
      <li>48710 Orchard Rd</li>
      <li>Harbor Glen fl 30912</li>
      <li>555 904 3826</li>
    </ul>

    <div class="web">
      <div class="web-address">www.fernfluffboutique-example.com</div>
      <div class="web-note">online booking available</div>
    </div>
  </div>
</body>
</html>
```